Seventy Crumbs needs a business card

Seventy Crumbs needs an attractive, playful, and exciting business card design to attract potential buyers. I have included our logo, label, and social media design files along with the fonts and colors for ideas. For the logo file, please only pay attention to the purple background with white text. I want a card with premium matte and metallic finish. I want my name included, e-mail, and phone number. The logo must be included, and then use the label design and social media design files to add creativity to the design. Only the fonts that are provided should be used as well.

Name: Gregory Talliston
Phone: 555-417-2086
E-mail: gtalliston@seventycrumbs.example

Contact Information for Business Card

I want a card with premium matte and metallic finish. I want my name included, e-mail, and phone number. The logo must be included, and then use the label design and social media design files to add creativity to the design. Only the fonts that are provided should be used as well.

Name: Gregory Talliston
Phone: 555-417-2086

Colors
6b449b

Requirements
Must have
• My logo, my fonts, my colors, my designs to some degree, and my character

```html
<!DOCTYPE html>
<html lang="en">
<head>
<meta charset="utf-8">
<title>Seventy Crumbs — Business Card</title>
<link rel="stylesheet" href="https://fonts.googleapis.com/css2?family=Aladin&family=Open+Sans:ital,wght@1,700&family=Dancing+Script:wght@500&display=swap">
<style>
  :root {
    --stage: #e6e6e8;
    --card-purple: #3f2a62;
    --card-purple-deep: #34204f;
    --skyline: #2e1c47;
    --name-gold: #f3d51b;
    --ink-white: #ffffff;
    --label-ink: #1c1c1c;
  }
  * { box-sizing: border-box; margin: 0; padding: 0; }
  html, body { width: 1200px; height: 959px; overflow: hidden; }
  body { background: var(--stage); position: relative; font-family: "Aladin", cursive; }

  .side-label {
    position: absolute;
    font-family: "Open Sans", sans-serif;
    font-style: italic; font-weight: 700;
    font-size: 20px; letter-spacing: 3px;
    color: var(--label-ink);
  }
  .side-label--back { left: 850px; top: 96px; }
  .side-label--front { left: 850px; top: 462px; }

  .card {
    position: absolute;
    width: 720px; height: 411px;
    background: linear-gradient(160deg, var(--card-purple) 0%, var(--card-purple-deep) 100%);
    overflow: hidden;
    box-shadow: 0 8px 24px rgba(0,0,0,0.18);
  }
  .card--back { left: 80px; top: 40px; }
  .card--front { left: 400px; top: 508px; }

  .skyline-band {
    position: absolute; left: 0; right: 0; bottom: 0; height: 150px;
    background: linear-gradient(180deg, rgba(46,28,71,0) 0%, var(--skyline) 70%);
  }
  .palace-glow {
    position: absolute; right: 40px; top: 40px; width: 380px; height: 371px;
    background: radial-gradient(ellipse at 50% 45%, rgba(78,56,112,0.55) 0%, rgba(63,42,98,0) 70%);
  }

  .brand-name {
    position: absolute;
    font-family: "Aladin", cursive;
    color: var(--ink-white);
    font-size: 46px; line-height: 1;
    text-align: center;
  }
  .card--back .brand-name { left: 0; right: 0; top: 170px; }
  .card--front .brand-name { left: 40px; top: 180px; width: 230px; font-size: 40px; }

  .contact {
    position: absolute; left: 300px; top: 120px;
  }
  .contact__name {
    font-family: "Aladin", cursive;
    color: var(--name-gold);
    font-size: 44px; line-height: 1.1;
    margin-bottom: 14px;
  }
  .contact__line {
    display: flex; align-items: center; gap: 12px;
    font-family: "Dancing Script", cursive;
    color: var(--ink-white);
    font-size: 22px; margin-bottom: 12px;
  }
  .contact__icon { width: 18px; height: 18px; flex: none; }
</style>
</head>
<body>
  <div class="side-label side-label--back">BACK SIDE</div>
  <div class="side-label side-label--front">FRONT SIDE</div>

  <section class="card card--back">
    <div class="skyline-band" role="img" aria-label="Silhouette of palace domes and minarets along the bottom edge"></div>
    <div class="brand-name">Seventy Crumbs</div>
  </section>

  <section class="card card--front">
    <div class="palace-glow" role="img" aria-label="Faint silhouette of a domed palace behind the contact details"></div>
    <div class="brand-name">Seventy Crumbs</div>
    <div class="contact">
      <div class="contact__name">Gregory Talliston</div>
      <div class="contact__line">
        <svg class="contact__icon" viewBox="0 0 18 18" aria-hidden="true">
          <circle cx="9" cy="9" r="9" fill="#fff"/>
          <rect x="6" y="4" width="6" height="10" rx="1.2" fill="#3f2a62"/>
        </svg>
        <span>555-417-2086</span>
      </div>
      <div class="contact__line">
        <svg class="contact__icon" viewBox="0 0 18 18" aria-hidden="true">
          <circle cx="9" cy="9" r="9" fill="#fff"/>
          <rect x="4.5" y="5.5" width="9" height="7" rx="1" fill="#3f2a62"/>
          <path d="M4.8 6 L9 9.3 L13.2 6" stroke="#fff" stroke-width="0.9" fill="none"/>
        </svg>
        <span>gtalliston@seventycrumbs.example</span>
      </div>
    </div>
  </section>
</body>
</html>
```